we are an outdoor outlet in a Nile Club that has a variety of outlets. The Club is called Brookhaven and is located in Cairo, Egypt. This garden menu will include cuisines from the Mediterranean, Asia and Texmex. we need a menu that is colorful and would fit an A3 size, back and front are to be used. Attached is the old menu currently in use (Garden Menu 2012.pdf is just for reference) and the new menu text for you to use is under the name Garden Menu Fall 2013
thank you.

```html
<!DOCTYPE html>
<html lang="en">
<head>
<meta charset="utf-8">
<title>Brookhaven Garden Menu</title>
<link href="https://fonts.googleapis.com/css2?family=Allura&family=Dancing+Script:wght@500;700&family=Raleway:wght@400;600;700&display=swap" rel="stylesheet">
<style>
  :root {
    --backdrop: #ece9e4;
    --paper: #ffffff;
    --stone: #e4e0da;
    --stone-soft: #f1efeb;
    --olive: #a9b437;
    --rose: #c7365f;
    --rose-soft: #e8a3b6;
    --plum: #6b2c3a;
    --teal: #3a8fb5;
    --ink: #5b4a46;
    --ink-soft: #8f8380;
  }
  * { box-sizing: border-box; margin: 0; padding: 0; }
  html, body { width: 1200px; height: 800px; overflow: hidden; }
  body {
    background: var(--backdrop);
    font-family: "Raleway", sans-serif;
    color: var(--ink);
    display: flex;
    align-items: center;
    justify-content: center;
    gap: 30px;
  }
  .sheet {
    width: 570px;
    height: 403px;
    background: var(--paper);
    display: grid;
    grid-template-columns: repeat(3, 1fr);
    box-shadow: 0 6px 18px rgba(60, 45, 35, .18);
    overflow: hidden;
  }
  .panel {
    position: relative;
    padding: 12px 13px 8px;
    display: flex;
    flex-direction: column;
    min-width: 0;
    border-right: 1px dashed #ece8e3;
  }
  .panel:last-child { border-right: none; }
  .panel--stone { background: var(--stone-soft); }
  .corner-title {
    font-family: "Allura", cursive;
    font-size: 26px;
    line-height: 1.05;
    color: var(--olive);
    margin-bottom: 2px;
    white-space: nowrap;
  }
  .corner-title--plum { color: var(--plum); }
  .corner-title--long { font-size: 21px; }
  .section-head {
    font-family: "Raleway", sans-serif;
    font-weight: 700;
    font-size: 9px;
    letter-spacing: .3px;
    color: var(--rose);
    margin: 5px 0 3px;
  }
  .section-head--teal { color: var(--teal); }
  .section-head--olive { color: var(--olive); }
  .menu-item { margin-bottom: 3px; }
  .item-line {
    display: flex;
    align-items: baseline;
    gap: 3px;
  }
  .item-name {
    font-family: "Dancing Script", cursive;
    font-weight: 700;
    font-size: 11px;
    color: var(--plum);
    white-space: nowrap;
  }
  .item-leader {
    flex: 1;
    border-bottom: 1px dotted #c9c1bd;
    transform: translateY(-2px);
  }
  .item-price {
    font-size: 6px;
    font-weight: 600;
    color: var(--ink-soft);
    white-space: nowrap;
  }
  .item-desc {
    font-size: 6px;
    line-height: 1.3;
    color: var(--ink-soft);
  }
  .list-item {
    display: flex;
    align-items: center;
    gap: 4px;
    font-size: 6.5px;
    margin-bottom: 3px;
    color: var(--ink);
  }
  .list-item::before {
    content: "";
    width: 4px; height: 4px;
    border-radius: 50%;
    background: var(--rose);
    flex: none;
  }
  .list-item .item-leader { transform: translateY(-1px); }
  .art {
    border-radius: 4px;
    flex: none;
  }
  .art--bamboo {
    height: 62px;
    margin: 4px 0 6px;
    background: linear-gradient(100deg, #eef0dc 0%, #d9dcc0 40%, #f1dbe3 75%, #efece6 100%);
  }
  .art--cactus {
    height: 70px;
    margin: 6px 0;
    background: linear-gradient(120deg, #e9ecc7 0%, #c9d174 45%, #e7b7c6 80%, #f0ece6 100%);
  }
  .art--blossom {
    height: 48px;
    margin-top: auto;
    background: linear-gradient(90deg, #f1efeb 0%, #e5e2dc 55%, #ecdfe3 100%);
  }
  .art--garden {
    flex: 1;
    margin-top: 10px;
    background: linear-gradient(135deg, #eef0d4 0%, #e9c2cf 45%, #d45a7e 70%, #f3e4e8 100%);
  }
  .divider {
    height: 6px;
    margin: 5px 0 3px;
  }
  .cover {
    background: var(--stone);
    align-items: center;
    text-align: center;
  }
  .cover-title {
    font-family: "Allura", cursive;
    font-size: 40px;
    color: var(--rose);
    line-height: 1;
    margin-top: 22px;
  }
  .brand {
    display: flex;
    align-items: center;
    gap: 6px;
    margin-top: 18px;
  }
  .brand-dot {
    width: 14px; height: 14px;
    border-radius: 50%;
    background: var(--olive);
  }
  .brand-name {
    font-family: "Raleway", sans-serif;
    font-weight: 600;
    font-size: 17px;
    color: var(--plum);
  }
  .brand-sub {
    font-size: 6.5px;
    letter-spacing: 2px;
    color: var(--ink-soft);
    margin-top: 3px;
  }
  .cover .art--garden { width: 100%; }
  .toppings {
    font-size: 6px;
    color: var(--ink-soft);
    margin-bottom: 2px;
  }
  .toppings strong { color: var(--rose); font-weight: 700; }
</style>
</head>
<body>

<section class="sheet sheet--outside">
  <div class="panel">
    <h2 class="corner-title corner-title--long">Mediterranean Corner</h2>
    <h3 class="section-head">Soups</h3>
    <div class="menu-item"><div class="item-line"><span class="item-name">Tomato Basil</span><span class="item-leader"></span><span class="item-price">LE 28</span></div><p class="item-desc">roasted tomatoes, fresh basil, cream</p></div>
    <div class="menu-item"><div class="item-line"><span class="item-name">Chicken Cream</span><span class="item-leader"></span><span class="item-price">LE 30</span></div><p class="item-desc">creamy chicken with mushrooms</p></div>
    <div class="menu-item"><div class="item-line"><span class="item-name">Minestrone</span><span class="item-leader"></span><span class="item-price">LE 28</span></div><p class="item-desc">vegetables, beans and small pasta</p></div>
    <h3 class="section-head section-head--olive">Appetizers</h3>
    <div class="list-item">Hummus<span class="item-leader"></span><span class="item-price">LE 18</span></div>
    <div class="list-item">Baba Ghanoug<span class="item-leader"></span><span class="item-price">LE 18</span></div>
    <div class="list-item">Tabbouleh<span class="item-leader"></span><span class="item-price">LE 20</span></div>
    <div class="list-item">Stuffed Vine Leaves<span class="item-leader"></span><span class="item-price">LE 24</span></div>
    <div class="list-item">Falafel<span class="item-leader"></span><span class="item-price">LE 16</span></div>
    <div class="list-item">Cheese Sambousek<span class="item-leader"></span><span class="item-price">LE 22</span></div>
    <div class="list-item">Fried Calamari<span class="item-leader"></span><span class="item-price">LE 38</span></div>
    <div class="list-item">Mozzarella Sticks<span class="item-leader"></span><span class="item-price">LE 30</span></div>
    <h3 class="section-head">Salads</h3>
    <div class="menu-item"><div class="item-line"><span class="item-name">Caprese</span><span class="item-leader"></span><span class="item-price">LE 40</span></div><p class="item-desc">tomato, mozzarella, basil, olive oil</p></div>
    <div class="menu-item"><div class="item-line"><span class="item-name">Greek Salad</span><span class="item-leader"></span><span class="item-price">LE 36</span></div><p class="item-desc">feta, olives, cucumber, oregano</p></div>
    <div class="menu-item"><div class="item-line"><span class="item-name">Fresh Garden Salad</span><span class="item-leader"></span><span class="item-price">LE 30</span></div><p class="item-desc">mixed greens, lemon dressing</p></div>
    <div class="menu-item"><div class="item-line"><span class="item-name">Feta Salad</span><span class="item-leader"></span><span class="item-price">LE 34</span></div><p class="item-desc">watermelon, mint, balsamic</p></div>
  </div>

  <div class="panel">
    <h3 class="section-head">Pizza &amp; Pasta</h3>
    <div class="menu-item"><div class="item-line"><span class="item-name">Lasagna</span><span class="item-leader"></span><span class="item-price">LE 55</span></div><p class="item-desc">beef ragù, béchamel, mozzarella</p></div>
    <div class="menu-item"><div class="item-line"><span class="item-name">Pizza Margarita</span><span class="item-leader"></span><span class="item-price">LE 45</span></div><p class="item-desc">tomato sauce, mozzarella, basil</p></div>
    <div class="menu-item"><div class="item-line"><span class="item-name">Create your own pasta</span><span class="item-leader"></span><span class="item-price">LE 48</span></div><p class="item-desc">choose pasta and sauce</p></div>
    <p class="toppings"><strong>Toppings:</strong> mushrooms, olives, peppers, pepperoni, extra cheese</p>
    <svg class="divider" viewBox="0 0 160 6" preserveAspectRatio="none" aria-hidden="true">
      <line x1="0" y1="3" x2="160" y2="3" stroke="#e8a3b6" stroke-width="1"/>
      <circle cx="80" cy="3" r="2.5" fill="#c7365f"/>
    </svg>
    <h3 class="section-head section-head--olive">Sandwiches</h3>
    <div class="menu-item"><div class="item-line"><span class="item-name">Club Sandwich</span><span class="item-leader"></span><span class="item-price">LE 42</span></div><p class="item-desc">turkey, bacon, egg, cheddar</p></div>
    <div class="menu-item"><div class="item-line"><span class="item-name">Steak Sandwich</span><span class="item-leader"></span><span class="item-price">LE 55</span></div><p class="item-desc">grilled beef, onions, mustard mayo</p></div>
    <div class="menu-item"><div class="item-line"><span class="item-name">Tuna Melt</span><span class="item-leader"></span><span class="item-price">LE 38</span></div><p class="item-desc">tuna, cheddar, toasted bread</p></div>
    <div class="menu-item"><div class="item-line"><span class="item-name">Halloumi Panini</span><span class="item-leader"></span><span class="item-price">LE 36</span></div><p class="item-desc">grilled halloumi, tomato, pesto</p></div>
    <h3 class="section-head">Main Courses</h3>
    <div class="menu-item"><div class="item-line"><span class="item-name">Chicken Escalope</span><span class="item-leader"></span><span class="item-price">LE 65</span></div><p class="item-desc">breaded chicken, mashed potatoes</p></div>
    <div class="menu-item"><div class="item-line"><span class="item-name">Grilled Salmon</span><span class="item-leader"></span><span class="item-price">LE 95</span></div><p class="item-desc">lemon butter, vegetables</p></div>
    <div class="menu-item"><div class="item-line"><span class="item-name">Mixed Grill</span><span class="item-leader"></span><span class="item-price">LE 85</span></div><p class="item-desc">kofta, shish tawook, rice</p></div>
    <div class="menu-item"><div class="item-line"><span class="item-name">Fish Fillet</span><span class="item-leader"></span><span class="item-price">LE 70</span></div><p class="item-desc">herb crust, sautéed greens</p></div>
  </div>

  <div class="panel cover">
    <h1 class="cover-title">Garden Menu</h1>
    <div class="brand">
      <span class="brand-dot"></span>
      <span class="brand-name">Brookhaven</span>
    </div>
    <p class="brand-sub">NILE CLUB</p>
    <div class="art art--garden" role="img" aria-label="Illustration of pink blossoms, leaves and berry sprigs"></div>
  </div>
</section>

<section class="sheet sheet--inside">
  <div class="panel">
    <div class="art art--bamboo" role="img" aria-label="Illustration of bamboo stalks, chopsticks and a pink flower"></div>
    <h2 class="corner-title corner-title--plum">Asian Corner</h2>
    <h3 class="section-head">Salads &amp; Appetizers</h3>
    <div class="menu-item"><div class="item-line"><span class="item-name">Chicken Wonton Salad</span><span class="item-leader"></span><span class="item-price">LE 42</span></div><p class="item-desc">crisp lettuce, wonton strips, ginger dressing</p></div>
    <div class="menu-item"><div class="item-line"><span class="item-name">Chicken Sesame Noodle Salad</span><span class="item-leader"></span><span class="item-price">LE 45</span></div><p class="item-desc">egg noodles, peppers, toasted sesame dressing</p></div>
    <div class="menu-item"><div class="item-line"><span class="item-name">Spring Rolls</span><span class="item-leader"></span><span class="item-price">LE 28</span></div><p class="item-desc">vegetables wrapped and fried, sweet chili</p></div>
    <div class="menu-item"><div class="item-line"><span class="item-name">Indian Samosa</span><span class="item-leader"></span><span class="item-price">LE 26</span></div><p class="item-desc">spiced potato pastry with mint chutney</p></div>
    <h3 class="section-head section-head--olive">Main Courses</h3>
    <div class="menu-item"><div class="item-line"><span class="item-name">Mango Chicken Makhni</span><span class="item-leader"></span><span class="item-price">LE 68</span></div><p class="item-desc">creamy tomato sauce with mango, basmati rice</p></div>
    <div class="menu-item"><div class="item-line"><span class="item-name">Chicken Tandoori</span><span class="item-leader"></span><span class="item-price">LE 65</span></div><p class="item-desc">yogurt marinated chicken, naan and raita</p></div>
    <div class="menu-item"><div class="item-line"><span class="item-name">Thai Coconut Curry Shrimp</span><span class="item-leader"></span><span class="item-price">LE 90</span></div><p class="item-desc">red curry, coconut milk, jasmine rice</p></div>
    <div class="menu-item"><div class="item-line"><span class="item-name">Mongolian Beef</span><span class="item-leader"></span><span class="item-price">LE 80</span></div><p class="item-desc">sliced beef, scallions, sweet soy glaze</p></div>
  </div>

  <div class="panel">
    <h2 class="corner-title">Tex Mex</h2>
    <h3 class="section-head section-head--teal">Salads &amp; Appetizers</h3>
    <div class="menu-item"><div class="item-line"><span class="item-name">Caesar Salad</span><span class="item-leader"></span><span class="item-price">LE 38</span></div><p class="item-desc">romaine, parmesan, croutons, classic dressing</p></div>
    <div class="menu-item"><div class="item-line"><span class="item-name">Taco Salad</span><span class="item-leader"></span><span class="item-price">LE 42</span></div><p class="item-desc">beef, beans, cheddar, salsa in tortilla bowl</p></div>
    <div class="menu-item"><div class="item-line"><span class="item-name">Nachos</span><span class="item-leader"></span><span class="item-price">LE 34</span></div><p class="item-desc">tortilla chips, cheese sauce, jalapeños</p></div>
    <div class="art art--cactus" role="img" aria-label="Illustration of a patterned green cactus with pink flowers"></div>
    <h3 class="section-head">Main Courses &amp; Sandwiches</h3>
    <div class="menu-item"><div class="item-line"><span class="item-name">Quesadillas</span><span class="item-leader"></span><span class="item-price">LE 48</span></div><p class="item-desc">chicken or beef, peppers, melted cheese</p></div>
    <div class="menu-item"><div class="item-line"><span class="item-name">Mexican Burger</span><span class="item-leader"></span><span class="item-price">LE 55</span></div><p class="item-desc">beef patty, guacamole, jalapeños, fries</p></div>
    <div class="menu-item"><div class="item-line"><span class="item-name">Crispy Chicken Wrap</span><span class="item-leader"></span><span class="item-price">LE 45</span></div><p class="item-desc">fried chicken, lettuce, chipotle mayo</p></div>
    <div class="menu-item"><div class="item-line"><span class="item-name">Fajita Chicken Bay Combo</span><span class="item-leader"></span><span class="item-price">LE 70</span></div><p class="item-desc">sizzling chicken, tortillas, rice and beans</p></div>
  </div>

  <div class="panel panel--stone">
    <h2 class="corner-title corner-title--plum">Desserts</h2>
    <div class="list-item">Chocolate Fondant<span class="item-leader"></span><span class="item-price">LE 35</span></div>
    <div class="list-item">Cheesecake<span class="item-leader"></span><span class="item-price">LE 32</span></div>
    <div class="list-item">Fruit Salad<span class="item-leader"></span><span class="item-price">LE 25</span></div>
    <div class="list-item">Crème Caramel<span class="item-leader"></span><span class="item-price">LE 22</span></div>
    <div class="list-item">Ice Cream Scoops<span class="item-leader"></span><span class="item-price">LE 20</span></div>
    <div class="list-item">Apple Crumble<span class="item-leader"></span><span class="item-price">LE 30</span></div>
    <div class="art art--blossom" role="img" aria-label="Faint line illustration of white blossoms"></div>
  </div>
</section>

</body>
</html>
```